Tulmex Business Card

I already have the conplay logo. I need to develop a professional business card layout

Target Market(s)

Business

Industry/Entity Type

Business

Contact Information for Business Card

Company Name: Tulmex Limited

Font styles to use
Sans Serif

Colors

Designer to choose colors to be used in the design.

Requirements
Must have
• Use current logo
• Need two card size options:
• Small Card: 70mm x 28mm (Landscape)
• Square Card: 65mm x 65mm
Nice to have
• I will need 8-10 files for each name, number and email address (details to follow)

```html
<!DOCTYPE html>
<html lang="en">
<head>
<meta charset="utf-8">
<title>Tulmex Business Card</title>
<link href="https://fonts.googleapis.com/css2?family=Roboto:ital,wght@0,300;0,400;0,700;1,700&display=swap" rel="stylesheet">
<style>
  :root {
    --page-bg: #e9e7e3;
    --card-white: #ffffff;
    --card-dark: #1e1e1f;
    --card-dark-glow: #4a4a4c;
    --ink: #1b1b1b;
    --ink-soft: #3a3a3a;
    --brand: #7cc418;
    --pin: #6aaa1a;
    --phone: #e1251b;
    --mail: #1a88d6;
    --web-text: #d8d8d8;
  }
  * { margin: 0; padding: 0; box-sizing: border-box; }
  html, body { width: 1200px; height: 800px; overflow: hidden; }
  body {
    background: var(--page-bg);
    font-family: "Roboto", Arial, sans-serif;
    position: relative;
  }
  .card {
    position: absolute;
    box-shadow: 0 6px 18px rgba(0,0,0,0.18);
    overflow: hidden;
  }

  /* Square card: details side + brand side */
  .card-square {
    left: 60px; top: 170px;
    width: 460px; height: 460px;
    display: flex;
  }
  .details-side {
    position: relative;
    width: 46%;
    background: var(--card-white);
    padding: 118px 0 0 40px;
    color: var(--ink);
  }
  .pointer {
    position: absolute;
    left: 0; top: 128px;
    width: 0; height: 0;
    border-top: 12px solid transparent;
    border-bottom: 12px solid transparent;
    border-left: 18px solid var(--ink);
  }
  .person-name {
    font-weight: 300;
    font-size: 27px;
    line-height: 1.1;
    white-space: nowrap;
  }
  .person-role {
    font-weight: 700;
    font-style: italic;
    font-size: 12px;
    margin-top: 2px;
  }
  .company {
    margin-top: 112px;
    font-weight: 700;
    font-size: 15px;
    margin-left: 20px;
  }
  .contact-list { list-style: none; margin-left: 20px; margin-top: 4px; }
  .contact-list li {
    display: flex; align-items: flex-start; gap: 6px;
    font-size: 12px; line-height: 1.35; color: var(--ink-soft);
  }
  .contact-list li + li.gap { margin-top: 8px; }
  .contact-list svg { flex: 0 0 10px; margin-top: 2px; }

  .brand-side {
    width: 54%;
    background: radial-gradient(circle at 55% 45%, var(--card-dark-glow), var(--card-dark) 70%);
    display: flex; align-items: center; justify-content: center;
  }

  /* Landscape card: brand back */
  .card-landscape {
    left: 560px; top: 240px;
    width: 600px; height: 340px;
    background: radial-gradient(ellipse at 50% 42%, var(--card-dark-glow), var(--card-dark) 65%);
    display: flex; flex-direction: column; align-items: center; justify-content: center;
  }
  .wordmark {
    font-family: "Roboto", Arial, sans-serif;
    font-weight: 700;
    color: var(--brand);
    letter-spacing: 2px;
  }
  .brand-side .wordmark { font-size: 40px; }
  .card-landscape .wordmark { font-size: 64px; margin-top: 30px; }
  .web-address {
    margin-top: 48px;
    font-size: 15px;
    letter-spacing: 1.5px;
    color: var(--web-text);
  }
  .web-address strong { font-weight: 700; }
</style>
</head>
<body>

<section class="card card-square">
  <div class="details-side">
    <span class="pointer"></span>
    <p class="person-name">Marlow Keats</p>
    <p class="person-role">Manager Finance</p>
    <p class="company">Tulmex Limited</p>
    <ul class="contact-list">
      <li>
        <svg width="10" height="13" viewBox="0 0 10 13"><path d="M5 0a4.5 4.5 0 0 0-4.5 4.5C.5 8 5 13 5 13s4.5-5 4.5-8.5A4.5 4.5 0 0 0 5 0zm0 6.3a1.8 1.8 0 1 1 0-3.6 1.8 1.8 0 0 1 0 3.6z" fill="var(--pin)"/></svg>
        <span>48 Alder Row, Eastfield ON<br>Canada K2P4R8</span>
      </li>
      <li class="gap">
        <svg width="10" height="13" viewBox="0 0 10 13"><rect x="1" y="0.5" width="8" height="12" rx="1.2" fill="none" stroke="var(--phone)" stroke-width="1.4"/><rect x="4" y="10" width="2" height="1.2" fill="var(--phone)"/></svg>
        <span>(+) 555 218 4407</span>
      </li>
      <li>
        <svg width="10" height="13" viewBox="0 0 10 13"><rect x="0.5" y="3" width="9" height="7" fill="var(--mail)"/><path d="M0.5 3 5 7l4.5-4" fill="none" stroke="#fff" stroke-width="1"/></svg>
        <span>info@tulmex.com</span>
      </li>
    </ul>
  </div>
  <div class="brand-side">
    <span class="wordmark">TULMEX</span>
  </div>
</section>

<section class="card card-landscape">
  <span class="wordmark">TULMEX</span>
  <p class="web-address">www.<strong>tulmex</strong>.com</p>
</section>

</body>
</html>
```